We need motivational posters designed to be used in classrooms at a truck driving school. The purpose of the posters is to motivate the students.

I want the the quotes to be the main focal point of emphasis and our logo on the bottom of the poster for branding purposes.

I would like the images to be related to the trucking industry

Below are the quotes for the posters

Poster 1
"Start where you are. Use what you have. Do what you can."
-Delmar Quisby-

Poster 2
"The secret of getting ahead is getting started"
-Owen Farrow-

Poster 3
"Most effective way to do it, is to do it."
-Rosalind Pemberly-

Poster 4
"Set your goals big, and don't stop till you get there."
-Cy Whitlock-

Poster 5
"If you are not willing to learn, no one can help you. If you are determined to learn, no one can stop you."
-Unknown-

Poster 6
"The will to succeed is important, but what's more important is the will to prepare."
-Dougie Hallam-

THESE POSTERS SHOULD BE DESIGNED AS 18X24
LANDSCAPE AND PORTRAIT ORIENTATION

Industry/Entity Type

School

```html
<!DOCTYPE html>
<html lang="en">
<head>
<meta charset="utf-8">
<title>The Secret of Getting Ahead – Classroom Poster</title>
<link rel="stylesheet" href="https://fonts.googleapis.com/css2?family=Barlow:wght@300;800&family=Cinzel:wght@400&display=swap">
<style>
  :root {
    --sky-top: #3a3c46;
    --sky-mid: #2a2b31;
    --ground: #141517;
    --cab: #55575d;
    --cab-shadow: #2c2d31;
    --ink: #ffffff;
  }
  html, body {
    margin: 0;
    padding: 0;
    width: 1200px;
    height: 900px;
    overflow: hidden;
    background: var(--ground);
  }
  .poster {
    position: relative;
    width: 1200px;
    height: 900px;
    overflow: hidden;
  }
  .poster__photo {
    position: absolute;
    inset: 0;
    background:
      radial-gradient(ellipse 30% 48% at 52% 52%, var(--cab) 0%, var(--cab-shadow) 75%, rgba(0,0,0,0) 100%),
      radial-gradient(ellipse 18% 30% at 90% 50%, rgba(80,82,88,0.7), rgba(0,0,0,0) 100%),
      radial-gradient(ellipse 16% 40% at 8% 45%, rgba(60,62,68,0.6), rgba(0,0,0,0) 100%),
      linear-gradient(180deg, var(--sky-top) 0%, var(--sky-mid) 45%, var(--ground) 100%);
  }
  .poster__quote {
    position: absolute;
    inset: 0;
    width: 1200px;
    height: 900px;
  }
  .quote__light {
    font-family: "Barlow", sans-serif;
    font-weight: 300;
    font-size: 128px;
    fill: var(--ink);
  }
  .quote__bold {
    font-family: "Barlow", sans-serif;
    font-weight: 800;
    fill: var(--ink);
  }
  .quote__bold--ahead { font-size: 90px; }
  .quote__bold--started { font-size: 98px; }
  .quote__swoosh { fill: var(--ink); }
  .quote__author {
    font-family: "Cinzel", serif;
    font-weight: 400;
    font-size: 62px;
    fill: var(--ink);
  }
</style>
</head>
<body>
  <main class="poster">
    <div class="poster__photo" role="img" aria-label="Trucking photograph: a white semi truck cab with tall chrome exhaust stacks, parked between trailers under a stormy sky, darkened behind the quote"></div>

    <svg class="poster__quote" viewBox="0 0 1200 900" aria-label="The secret of getting ahead is getting started – Owen Farrow">
      <text class="quote__light" x="95" y="128" textLength="955" lengthAdjust="spacing">THE SECRET</text>
      <text class="quote__light" x="88" y="243" textLength="970" lengthAdjust="spacing">OF GETTING</text>

      <path class="quote__swoosh" d="M160 350 Q240 330 318 316 L316 340 Q240 342 160 350 Z"/>
      <text class="quote__bold quote__bold--ahead" x="322" y="362" textLength="505" lengthAdjust="spacing">AHEAD</text>
      <path class="quote__swoosh" d="M975 350 Q900 330 850 316 L852 340 Q905 342 975 350 Z"/>

      <text class="quote__light" x="92" y="603" textLength="966" lengthAdjust="spacing">IS GETTING</text>

      <path class="quote__swoosh" d="M160 706 Q195 688 220 672 L218 698 Q192 700 160 706 Z"/>
      <text class="quote__bold quote__bold--started" x="222" y="724" textLength="700" lengthAdjust="spacing">STARTED</text>
      <path class="quote__swoosh" d="M1060 706 Q1000 688 930 672 L932 698 Q1000 700 1060 706 Z"/>

      <text class="quote__author" x="528" y="842" textLength="522" lengthAdjust="spacingAndGlyphs">- OWEN FARROW</text>
    </svg>
  </main>
</body>
</html>
```